Money Mindset Podcast needs fun, creative cover art

Launching a new podcast called 'Turning the Page on Savings' - aimed at an audience 30-50 who are interested in the practicalities of managing their money but also the more mental and emotional aspects.
Looking for something not too serious, warm and friendly.

Must be easy to read on phone screens
3000 x 3000 in size
Avoid currency symbols $, £ etc, as may have an international audience

Target Market(s)

Podcast listeners age 30-50 starting in the UK but then worldwide. Probably 60:40 female bias

Industry/Entity Type

Life Coaching

Font styles to use
Serif
Sans Serif

Colors
cadf82
fee18a
acd037
85cae6
eea4c8
f59195
85acd3

Requirements
Must have
• Simple, clear design. Easy to read on variety of devices. 3000 x 3000
Appeal to those with a spiritual or emotional interests
Nice to have
• Stand out among other money related podcasts
Maybe play around with clouds, lightbulbs and clearing skies
Should not have
• Currency symbols such as $ or £
Be too corporate or bank like
Stock images

```html
<!DOCTYPE html>
<html lang="en">
<head>
<meta charset="utf-8">
<title>Money Mindset Podcast – Cover Art Samples</title>
<link href="https://fonts.googleapis.com/css2?family=DM+Serif+Display:ital@0;1&family=Montserrat:wght@400;500;600&display=swap" rel="stylesheet">
<style>
  :root {
    --sheet: #1e1e1e;
    --header: #000000;
    --ink-light: #ffffff;
    --charcoal: #2f2f2f;
    --lime: #acd037;
    --soft-lime: #cadf82;
    --sky: #85cae6;
    --coral: #f59195;
    --pink: #eea4c8;
    --butter: #fee18a;
    --steel-blue: #85acd3;
    --label: #e8e8e8;
  }
  * { margin: 0; padding: 0; box-sizing: border-box; }
  html, body { width: 938px; height: 1200px; overflow: hidden; }
  body {
    background: var(--sheet);
    font-family: "Montserrat", Arial, sans-serif;
    position: relative;
  }
  .sheet-header {
    position: absolute; left: 0; top: 0;
    width: 938px; height: 93px;
    background: var(--header);
    display: flex; align-items: center; justify-content: center;
  }
  .sheet-title {
    color: var(--ink-light);
    font-weight: 500;
    font-size: 22px;
    letter-spacing: 10.5px;
    padding-left: 10px;
  }
  .sample-label {
    position: absolute; left: 37px;
    color: var(--label);
    font-weight: 500;
    font-size: 13px;
    letter-spacing: 5px;
  }
  .sample-label--one { top: 140px; }
  .sample-label--two { top: 691px; }

  .cover {
    position: absolute; left: 37px;
    width: 426px; height: 426px;
    overflow: hidden;
  }
  .cover--one { top: 169px; }
  .cover--two { top: 719px; }

  .cover-art { position: absolute; inset: 0; }
  .cover--one .cover-art {
    background: radial-gradient(ellipse 62% 78% at 60% 48%,
      var(--charcoal) 0 74%, var(--lime) 82%, var(--coral) 92%);
  }
  .cover--two .cover-art {
    background: linear-gradient(90deg,
      var(--steel-blue) 0 6%, var(--butter) 16%, var(--coral) 28%,
      var(--charcoal) 42% 90%, var(--steel-blue) 100%);
  }

  .cover-title {
    position: absolute;
    display: flex; flex-direction: column;
    font-weight: 400;
  }
  .cover--one .cover-title { left: 92px; top: 96px; align-items: flex-start; }
  .cover--two .cover-title { right: 44px; top: 104px; align-items: flex-end; text-align: right; }

  .title-main {
    font-family: "DM Serif Display", Georgia, serif;
    color: var(--ink-light);
    font-size: 68px;
    line-height: 0.98;
  }
  .title-main em {
    font-style: italic;
    color: var(--soft-lime);
  }
  .title-rule {
    width: 64px; height: 3px;
    margin: 22px 0 16px;
    background: var(--pink);
  }
  .title-sub {
    font-family: "Montserrat", Arial, sans-serif;
    font-weight: 600;
    font-size: 17px;
    letter-spacing: 6px;
    color: var(--butter);
  }
</style>
</head>
<body>
  <header class="sheet-header">
    <h1 class="sheet-title">MONEY MINDSET PODCAST _3000 X 3000</h1>
  </header>

  <p class="sample-label sample-label--one">SAMPLE 1</p>
  <section class="cover cover--one">
    <div class="cover-art" role="img" aria-label="Illustration: layered dark head silhouette in profile with lime and coral outlines on a coral background"></div>
    <h2 class="cover-title">
      <span class="title-main">Turning<br>the <em>Page</em></span>
      <span class="title-rule"></span>
      <span class="title-sub">ON SAVINGS</span>
    </h2>
  </section>

  <p class="sample-label sample-label--two">SAMPLE 2</p>
  <section class="cover cover--two">
    <div class="cover-art" role="img" aria-label="Illustration: three stacked head silhouettes in yellow, coral and charcoal on a soft blue background"></div>
    <h2 class="cover-title">
      <span class="title-main">Turning<br>the <em>Page</em></span>
      <span class="title-rule"></span>
      <span class="title-sub">ON SAVINGS</span>
    </h2>
  </section>
</body>
</html>
```